Brisk Harbour Finance Business Cards

Looking for a business card for a new mortgage broking business. Name of the business is Brisk Harbour Finance. Purpose of the business is to build trust and strong relationships with clients to then assist them with your mortgage lending needs. Most relationships within the business start off as an enquiry, and then can evolve into a 10+ year relationship, servicing clients from purchasing a new home to then upgrading for their family and even then assisting their children with their first home purchase. Business card should communicate financial security and trust.

Target Market(s)

Targeting professional clients who are looking to build a relationship with a knowledgeable mortgage professional

Industry/Entity Type

Finance - Home Loans

Contact Information for Business Card

Peter Holcroft, Director, mobile: 0471 926058, email:peter@briskharbourfinance.com.au, website: www.briskharbourfinance.com.au

Font styles to use
Sans Serif

Requirements
Must have
• On the front: Must have company logo, contact details as above. On the back: slogan, 'full of choices, free of stress', plus listing services offered: home loans, investment loans, first home buyers, refinancing, car finance

```html
<!DOCTYPE html>
<html lang="en">
<head>
<meta charset="utf-8">
<title>Brisk Harbour Finance — Business Cards</title>
<link href="https://fonts.googleapis.com/css2?family=Montserrat:wght@600;700&family=Lato:wght@400;700&display=swap" rel="stylesheet">
<style>
  :root {
    --navy: #0d5079;
    --amber: #f2a31f;
    --paper: #ffffff;
    --ink-grey: #6f6f73;
    --rule-grey: #8a8a8e;
    --backdrop: #e7e8ea;
    --soft-white: rgba(255,255,255,0.82);
  }
  * { box-sizing: border-box; margin: 0; padding: 0; }
  html, body { width: 1200px; height: 952px; overflow: hidden; }
  body {
    background: var(--backdrop);
    position: relative;
    font-family: "Lato", Arial, sans-serif;
  }
  .card {
    position: absolute;
    left: 290px;
    width: 620px;
    height: 344px;
    border-radius: 4px;
    box-shadow: 0 6px 18px rgba(0,0,0,0.12);
    overflow: hidden;
  }
  .card--front { top: 102px; background: var(--paper); }
  .card--back  { top: 506px; background: var(--navy); }

  /* Front */
  .wordmark {
    position: absolute;
    left: 44px;
    top: 36px;
    font-family: "Montserrat", Arial, sans-serif;
    font-weight: 700;
    color: var(--navy);
    font-size: 30px;
    line-height: 1.02;
    letter-spacing: 0.5px;
    text-transform: uppercase;
  }
  .contact-list {
    position: absolute;
    left: 44px;
    top: 150px;
    list-style: none;
  }
  .contact-item {
    display: flex;
    align-items: center;
    gap: 9px;
    font-size: 13px;
    color: var(--ink-grey);
    height: 26px;
  }
  .contact-icon {
    width: 17px;
    height: 17px;
    background: var(--amber);
    border-radius: 3px;
    display: flex;
    align-items: center;
    justify-content: center;
    flex: none;
  }
  .contact-icon svg { width: 11px; height: 11px; }
  .holder {
    position: absolute;
    right: 44px;
    top: 160px;
    text-align: right;
  }
  .holder-name {
    font-family: "Montserrat", Arial, sans-serif;
    font-weight: 700;
    font-size: 24px;
    letter-spacing: 2px;
    text-transform: uppercase;
    color: var(--navy);
    white-space: nowrap;
  }
  .holder-name .surname { color: var(--amber); }
  .holder-role {
    margin-top: 4px;
    font-size: 15px;
    color: var(--ink-grey);
    letter-spacing: 0.5px;
  }
  .holder-rule {
    margin: 6px 0 0 auto;
    width: 90px;
    height: 2px;
    background: var(--rule-grey);
  }

  /* Back */
  .edge-tab {
    position: absolute;
    width: 22px;
    background: var(--amber);
  }
  .edge-tab--left  { left: 0; top: 70px; height: 140px; border-radius: 0 8px 8px 0; }
  .edge-tab--right { right: 0; top: 150px; height: 170px; border-radius: 8px 0 0 8px; }
  .back-content {
    position: absolute;
    inset: 0 60px;
    display: flex;
    flex-direction: column;
    align-items: center;
    justify-content: center;
    gap: 22px;
  }
  .brand-lockup {
    display: flex;
    align-items: center;
    gap: 16px;
  }
  .brand-square {
    width: 46px;
    height: 46px;
    background: var(--amber);
    border-radius: 6px;
  }
  .brand-name {
    font-family: "Montserrat", Arial, sans-serif;
    font-weight: 700;
    color: var(--paper);
    font-size: 30px;
    line-height: 1.02;
    letter-spacing: 0.5px;
    text-transform: uppercase;
  }
  .slogan {
    font-family: "Montserrat", Arial, sans-serif;
    font-weight: 600;
    font-size: 16px;
    letter-spacing: 1px;
    color: var(--amber);
    text-transform: lowercase;
  }
  .service-list {
    list-style: none;
    display: flex;
    flex-wrap: wrap;
    justify-content: center;
    gap: 6px 14px;
    max-width: 480px;
  }
  .service-item {
    display: flex;
    align-items: center;
    gap: 6px;
    font-size: 12px;
    font-weight: 700;
    letter-spacing: 1px;
    text-transform: uppercase;
    color: var(--soft-white);
    white-space: nowrap;
  }
  .service-item::before {
    content: "";
    width: 6px;
    height: 6px;
    border-radius: 50%;
    background: var(--amber);
  }
</style>
</head>
<body>

  <section class="card card--front" aria-label="Business card front">
    <div class="wordmark">Brisk<br>Harbour<br>Finance</div>

    <ul class="contact-list">
      <li class="contact-item">
        <span class="contact-icon">
          <svg viewBox="0 0 12 12" aria-hidden="true"><path d="M3 1.5l1.6 2.2-1 1.1c.6 1.2 1.5 2.1 2.7 2.7l1.1-1 2.2 1.6-.9 1.9C5.2 9.8 2.2 6.8 1.1 2.4z" fill="#fff"/></svg>
        </span>
        0471 926058
      </li>
      <li class="contact-item">
        <span class="contact-icon">
          <svg viewBox="0 0 12 12" aria-hidden="true"><rect x="1" y="2.5" width="10" height="7" fill="none" stroke="#fff" stroke-width="1.2"/><path d="M1 2.5l5 4 5-4" fill="none" stroke="#fff" stroke-width="1.2"/></svg>
        </span>
        peter@briskharbourfinance.com.au
      </li>
      <li class="contact-item">
        <span class="contact-icon">
          <svg viewBox="0 0 12 12" aria-hidden="true"><path d="M6 1a3.3 3.3 0 0 0-3.3 3.3C2.7 7 6 11 6 11s3.3-4 3.3-6.7A3.3 3.3 0 0 0 6 1zm0 4.5a1.2 1.2 0 1 1 0-2.4 1.2 1.2 0 0 1 0 2.4z" fill="#fff"/></svg>
        </span>
        www.briskharbourfinance.com.au
      </li>
    </ul>

    <div class="holder">
      <div class="holder-name">Peter <span class="surname">Holcroft</span></div>
      <div class="holder-role">Managing Director</div>
      <div class="holder-rule"></div>
    </div>
  </section>

  <section class="card card--back" aria-label="Business card back">
    <span class="edge-tab edge-tab--left"></span>
    <span class="edge-tab edge-tab--right"></span>
    <div class="back-content">
      <div class="brand-lockup">
        <span class="brand-square"></span>
        <div class="brand-name">Brisk<br>Harbour<br>Finance</div>
      </div>
      <p class="slogan">full of choices, free of stress</p>
      <ul class="service-list">
        <li class="service-item">Home Loans</li>
        <li class="service-item">Investment Loans</li>
        <li class="service-item">First Home Buyers</li>
        <li class="service-item">Refinancing</li>
        <li class="service-item">Car Finance</li>
      </ul>
    </div>
  </section>

</body>
</html>
```